Mondaxe custom business card design

Need a authentic, innovative business card design for a new mobile app business. I am uploading a few screen images from our app for you to view. I would like app design theme to match business card design. I can also send logo images.

```html
<!DOCTYPE html>
<html lang="en">
<head>
<meta charset="utf-8">
<title>Mondaxe Business Card</title>
<link rel="stylesheet" href="https://fonts.googleapis.com/css2?family=Archivo+Black&family=Work+Sans:wght@400;500&display=swap">
<style>
  :root {
    --stage: #1c1c1e;
    --card: #272628;
    --card-deep: #1f1e20;
    --purple: #663399;
    --white: #ffffff;
    --soft: #e9e6ee;
  }
  * { margin: 0; padding: 0; box-sizing: border-box; }
  html, body { width: 1200px; height: 900px; overflow: hidden; background: var(--stage); }
  .canvas {
    width: 1200px; height: 900px;
    display: flex; flex-direction: column; align-items: center; justify-content: center; gap: 40px;
  }
  .card {
    width: 630px; height: 360px; position: relative; overflow: hidden;
    background: var(--card);
    box-shadow: 0 18px 40px rgba(0,0,0,0.45);
  }
  /* back */
  .card-back .texture {
    position: absolute; inset: 0;
    background: radial-gradient(ellipse at 55% 55%, #353437 0%, var(--card-deep) 75%);
  }
  .back-mark {
    position: absolute; left: 50%; top: 50%; transform: translate(-50%, -50%);
    display: flex; align-items: center; gap: 10px;
    font-family: "Work Sans", sans-serif; font-weight: 500; font-size: 20px; color: var(--white);
  }
  .back-mark .dot { width: 22px; height: 22px; border-radius: 50%; background: var(--purple); }
  /* front */
  .brand {
    position: absolute; left: 46px; top: 34px;
    font-family: "Archivo Black", sans-serif; font-size: 56px; line-height: 1; color: var(--purple);
    letter-spacing: 0.5px;
  }
  .tagline {
    position: absolute; left: 48px; top: 104px; width: 300px;
    font-family: "Work Sans", sans-serif; font-size: 15px; line-height: 1.3; color: var(--soft);
    letter-spacing: 0.4px;
  }
  .person { position: absolute; left: 48px; top: 176px; font-family: "Work Sans", sans-serif; }
  .person .name { font-size: 24px; font-weight: 500; color: var(--purple); text-transform: uppercase; letter-spacing: 0.6px; }
  .person .role { font-size: 18px; color: var(--white); margin-top: 2px; }
  .contacts {
    position: absolute; left: 40px; top: 256px; list-style: none;
    font-family: "Work Sans", sans-serif; font-size: 17px; color: var(--white);
  }
  .contacts li { display: flex; align-items: center; gap: 10px; height: 26px; letter-spacing: 0.4px; }
  .contacts svg { width: 14px; height: 14px; flex: none; }
  .emblem {
    position: absolute; left: 348px; top: 62px; width: 250px; height: 250px; border-radius: 50%;
    background: var(--purple);
    display: flex; align-items: center; justify-content: center;
    font-family: "Work Sans", sans-serif; font-weight: 500; font-size: 34px; color: var(--white);
  }
</style>
</head>
<body>
<main class="canvas">
  <section class="card card-back" aria-label="Card back">
    <div class="texture" role="img" aria-label="Faint repeating brand pattern across a dark card"></div>
    <div class="back-mark"><span class="dot"></span>Mondaxe</div>
  </section>

  <section class="card card-front" aria-label="Card front">
    <h1 class="brand">Mondaxe</h1>
    <p class="tagline">A Innovative &amp; Virtual Information Exchange Community</p>
    <div class="person">
      <p class="name">Jordan Hale</p>
      <p class="role">COO/Co-founder</p>
    </div>
    <ul class="contacts">
      <li>
        <svg viewBox="0 0 16 16" aria-hidden="true"><path fill="var(--purple)" d="M4 1.5l2.2 2.8-1.3 1.6c.9 2 2.4 3.5 4.4 4.4l1.6-1.3 2.8 2.2-1.2 2.2C7.6 13.2 2.8 8.4 1.6 3.5z"/></svg>
        555-302-7819
      </li>
      <li>
        <svg viewBox="0 0 16 16" aria-hidden="true"><rect x="1.5" y="3.5" width="13" height="9" fill="none" stroke="var(--purple)" stroke-width="1.4"/><path d="M1.5 3.5L8 9l6.5-5.5" fill="none" stroke="var(--purple)" stroke-width="1.4"/></svg>
        jordan.hale@mondaxe.com
      </li>
      <li>
        <svg viewBox="0 0 16 16" aria-hidden="true"><g fill="none" stroke="var(--purple)" stroke-width="1.3"><circle cx="8" cy="8" r="6.5"/><ellipse cx="8" cy="8" rx="3" ry="6.5"/><path d="M1.5 8h13M2.5 5h11M2.5 11h11"/></g></svg>
        www.mondaxe.com
      </li>
    </ul>
    <div class="emblem">Mondaxe</div>
  </section>
</main>
</body>
</html>
```